Web Design Project

Please take a look at my current aged website www.marlowpeoplesupport.example and my newly designed logo and business cards. I would like a new fresh updated look to my website and my new designs incorporated.
Updates

  Good Morning Everyone

Due to an Austrralian licencing issue I have had to have my logo slightly redesigned.

Would you please be able to look at the newly uploaded files and revise your designs.

Thanks so much.  I am very happy with the calibre and quality of the designs so far.

kind Regards

Tessa

Industry/Entity Type

Business

Requirements
Must have
• the exisiting pages and fresh new graphics and a real commitment to my palette of lime green, turqouise and black.

```html
<!DOCTYPE html>
<html lang="en">
<head>
<meta charset="utf-8">
<title>Marlow Consulting – Human Resources and Recruitment Solutions</title>
<link rel="stylesheet" href="https://fonts.googleapis.com/css2?family=Open+Sans:ital,wght@0,400;0,600;0,700;1,400&display=swap">
<style>
:root{
  --lime:#6cbf45;
  --lime-dark:#4fa52f;
  --turquoise:#149fc9;
  --turquoise-deep:#0c8db5;
  --ink:#2a2a2a;
  --text:#474747;
  --muted:#8a8a8a;
  --band:#efefef;
  --login-band:#3b3b3b;
  --footer:#2a2a2a;
  --white:#ffffff;
}
*{box-sizing:border-box;margin:0;padding:0}
html,body{width:1091px;height:1200px;overflow:hidden;background:var(--white)}
body{font-family:"Open Sans",Arial,sans-serif;color:var(--text)}
.page{position:relative;width:1000px;height:1100px;transform:scale(1.091);transform-origin:0 0}
.abs{position:absolute}

.top-strip{left:0;top:0;width:1000px;height:8px;background:var(--lime)}

.brand{left:30px;top:35px;display:flex;align-items:center;gap:8px}
.brand-mark{width:56px;height:56px;border-radius:50%;background:var(--turquoise)}
.brand-name{font-size:25px;font-weight:600;color:var(--turquoise);line-height:1;letter-spacing:-.3px}
.brand-tag{font-size:7px;color:var(--ink);margin-top:3px;letter-spacing:.1px}

.search{left:797px;top:51px;width:178px;height:24px;border:1px solid #cfcfcf;border-radius:3px;background:linear-gradient(#f6f6f6,#fff);box-shadow:inset 0 1px 2px rgba(0,0,0,.12)}
.search span{position:absolute;left:14px;top:4px;font-size:11px;font-style:italic;color:#a0a0a0}
.search svg{position:absolute;right:6px;top:5px}

.nav-band{left:0;top:114px;width:1000px;height:283px;background:var(--band)}
.nav{left:36px;top:114px;height:48px;display:flex}
.nav a{display:flex;align-items:center;padding:0 27px;font-size:13px;color:#4a4a4a;text-decoration:none;border-right:1px solid #dedede;height:48px}
.nav a:last-child{border-right:0}
.nav a.active{background:linear-gradient(#dcdcdc,#f4f4f4);color:#111;padding:0 35px;border-right:0}
.social{top:124px;width:28px;height:28px;border-radius:3px}
.social.one{left:894px;background:#3b5b98}
.social.two{left:935px;background:#2aa3dc}

.slider{left:36px;top:168px;width:928px;height:283px;border:6px solid var(--turquoise);box-shadow:0 6px 8px -4px rgba(0,0,0,.45);overflow:hidden;background:linear-gradient(100deg,#7fd3f3 0%,#c8ecfb 40%,#f3f7fb 65%,#eef4f8 100%)}
.slider-scene{right:0;top:0;width:400px;height:271px;background:linear-gradient(180deg,#e9eef3 0%,#c9d1d9 55%,#39414a 100%);opacity:.85}
.slider-wave{left:180px;top:-40px;width:360px;height:90px;border-radius:50%;background:rgba(40,160,230,.45)}
.slide-kicker{left:145px;top:104px;font-size:21px;color:#1f1f1f;letter-spacing:.3px}
.slide-title{left:145px;top:132px;font-size:40px;color:#1f1f1f;line-height:1}
.slide-title small{font-size:20px;letter-spacing:.3px}
.dots{left:28px;top:237px;display:flex;gap:17px;align-items:center}
.dots i{display:block;width:12px;height:12px;border-radius:50%;background:#333}
.dots i.on{background:#fff;border:3px solid var(--lime);width:16px;height:16px;margin-right:-4px}

.welcome h1{font-size:20px;font-weight:400;color:var(--lime-dark);letter-spacing:.2px}
.welcome{left:35px;top:477px;width:697px}
.welcome p{margin-top:10px;font-size:10.6px;line-height:21px;text-align:justify;color:var(--text)}
.team-art{left:760px;top:480px;width:195px;height:130px;border-radius:6px;background:linear-gradient(135deg,#5b8fd6,#1f5fb8 60%,#d9d9d9)}

.service{top:696px;width:294px;height:239px;background:var(--turquoise);border-radius:6px;box-shadow:0 7px 8px -5px rgba(0,0,0,.45)}
.service h2{font-size:14.5px;font-weight:600;color:var(--white);text-align:center;margin-top:15px;letter-spacing:.1px}
.service ul{list-style:none;position:absolute;left:10px;top:46px;width:274px;height:170px;background:var(--white);border-radius:4px}
.service li{position:relative;padding:8px 12px 8px 38px;font-size:11.5px;line-height:16px;color:#3a3a3a;border-bottom:1px solid #e3e3e3}
.service li:before{content:"";position:absolute;left:21px;top:13px;border-left:7px solid #555;border-top:4px solid transparent;border-bottom:4px solid transparent}
.service li.short{padding-top:8px;padding-bottom:8px}
.service .more{position:absolute;left:0;bottom:3px;width:100%;text-align:center;font-size:11px;color:var(--white)}
.service-icon{top:640px;width:80px;height:64px;border-radius:8px}

.login-band{left:0;top:961px;width:1000px;height:57px;background:var(--login-band)}
.login-title{left:128px;top:980px;font-size:15.5px;color:var(--lime)}
.login-label{top:984px;font-size:11px;font-style:italic;color:#c9c9c9}
.login-input{top:978px;width:179px;height:24px;background:var(--white);border:1px solid #ccc;border-radius:2px}
.login-btn{left:804px;top:979px;width:68px;height:22px;background:linear-gradient(#7dd157,var(--lime-dark));border:1px solid #3e8a23;font-size:11.5px;font-weight:600;color:#1d3b10;display:flex;align-items:center;justify-content:center}

.footer{left:0;top:1018px;width:1000px;height:82px;background:var(--footer);text-align:center}
.footer nav{margin-top:20px;font-size:11px;color:#d4d4d4}
.footer nav span{margin:0 10px;color:#9a9a9a}
.footer p{margin-top:10px;font-size:11px;color:#d4d4d4}
</style>
</head>
<body>
<div class="page">
  <div class="abs top-strip"></div>

  <div class="abs brand">
    <div class="brand-mark"></div>
    <div>
      <div class="brand-name">Marlow Consulting</div>
      <div class="brand-tag">Human Resources and Recruitment Solutions</div>
    </div>
  </div>

  <div class="abs search">
    <span>Search</span>
    <svg width="11" height="11" viewBox="0 0 11 11"><circle cx="4.5" cy="4.5" r="3.3" fill="none" stroke="#aaa" stroke-width="1.4"/><line x1="7" y1="7" x2="10" y2="10" stroke="#aaa" stroke-width="1.6"/></svg>
  </div>

  <div class="abs nav-band"></div>
  <nav class="abs nav">
    <a class="active" href="#">HOME</a>
    <a href="#">OUR SERVICES</a>
    <a href="#">OUR CONSULTANTS</a>
    <a href="#">OUR FEES</a>
    <a href="#">CONTACT US</a>
  </nav>
  <div class="abs social one" aria-label="Social profile"></div>
  <div class="abs social two" aria-label="Social profile"></div>

  <div class="abs slider">
    <div class="abs slider-wave"></div>
    <div class="abs slider-scene" role="img" aria-label="Business team silhouettes in front of a world map"></div>
    <div class="abs slide-kicker">VIVAMUS ACCUMSAN</div>
    <div class="abs slide-title">CURABITUR <small>LAOREET</small></div>
    <div class="abs dots"><i class="on"></i><i></i><i></i><i></i><i></i></div>
  </div>

  <section class="abs welcome">
    <h1>WELCOME TO OUR SITE</h1>
    <p>Sed ut perspiciatis unde omnis iste natus error sit voluptatem accusantium doloremque laudantium, totam rem aperiam, eaque ipsa quae ab illo inventore veritatis et quasi architecto beatae vitae dicta sunt explicabo. Nemo enim ipsam voluptatem quia voluptas sit aspernatur aut odit aut fugit, sed quia consequuntur magni dolores eos qui ratione voluptatem sequi nesciunt. Neque porro quisquam est, qui dolorem ipsum quia dolor sit amet, consectetur, adipisci velit, sed quia non numquam eius modi tempora incidunt ut labore et dolore magnam aliquam quaerat voluptatem. Ut enim ad minima veniam.</p>
  </section>
  <div class="abs team-art" role="img" aria-label="Blue 3D lettering of the word team with small figures"></div>

  <div class="abs service-icon" style="left:142px;background:linear-gradient(#f0b25a,#5a9bd6)" role="img" aria-label="Two people icon"></div>
  <div class="abs service-icon" style="left:459px;background:linear-gradient(#e08a3c,#444)" role="img" aria-label="Consultant icon"></div>
  <div class="abs service-icon" style="left:777px;background:linear-gradient(#5aa6f0,#e03a3a 60%,#3cc046)" role="img" aria-label="Stacked coloured cubes icon"></div>

  <section class="abs service" style="left:34px">
    <h2>PEOPLE SYSTEMS AND PROCESSES</h2>
    <ul>
      <li>Attraction, Recruitment and Induction</li>
      <li>Remuneration, Benefits and Salary</li>
      <li>Talent Management and Retention</li>
      <li>Graduate Management</li>
      <li style="border-bottom:0">Performance Management and Planning</li>
    </ul>
    <div class="more">View more</div>
  </section>

  <section class="abs service" style="left:352px">
    <h2>EMPLOYEE RELATIONS</h2>
    <ul>
      <li>HR Function Review and Assessments</li>
      <li>Industrial Relations advice</li>
      <li>Contracts of Employment</li>
      <li>Industrial Award Service</li>
      <li style="border-bottom:0">Employee Entitlements</li>
    </ul>
    <div class="more">View more</div>
  </section>

  <section class="abs service" style="left:669px">
    <h2>ORGANISATION DEVELOPMENT</h2>
    <ul>
      <li>Policy &amp; Procedure Development and Auditing</li>
      <li>Organisation Evaluation and Re-design</li>
      <li>Culture and Values Asssessment and Planning</li>
    </ul>
    <div class="more">View more</div>
  </section>

  <div class="abs login-band"></div>
  <div class="abs login-title">Member Login</div>
  <div class="abs login-label" style="left:263px">Username :</div>
  <div class="abs login-input" style="left:329px"></div>
  <div class="abs login-label" style="left:538px">Password :</div>
  <div class="abs login-input" style="left:600px"></div>
  <div class="abs login-btn">LOG IN</div>

  <footer class="abs footer">
    <nav>Home<span>|</span>Our Services<span>|</span>Our Consultants<span>|</span>Our Fees<span>|</span>Contact&nbsp; Us</nav>
    <p>Copyright © 2012 www.marlowpeoplesupport.example &nbsp; All rights reserved.</p>
  </footer>
</div>
</body>
</html>
```